Larkspur Ridge Management - Business Cards

I need business cards. My current logo was designed by a designer at this site and I very much like and am happy with the results. I would like a business card that is trendy, unique, current yet professional. I deal with high net worth clients daily

Target Market(s)

Out of state investors looking to get into the rental market in Ohio

Industry/Entity Type

Property Management, Consulting

Contact Information for Business Card

Name, Title (Chief Financial Officer) office phone number (555) 817-3094 website address larkridgemgmt.example

Font styles to use
Sans Serif

Colors
0054AA
0677BA
7BADD7
CADEEF
E8F1F8
0094D4
00A9DD
6FCCEA
C7EBF8
E9F6FB
00AB8E
00BBA5
67D7C9
C6EFE9
E9F9F6

```html
<!DOCTYPE html>
<html lang="en">
<head>
<meta charset="utf-8">
<title>Larkspur Ridge Management – Business Cards</title>
<link rel="stylesheet" href="https://fonts.googleapis.com/css2?family=Inter:wght@400;500;700;800&display=swap">
<style>
  :root {
    --backdrop: #3b3431;
    --navy-deep: #0c1432;
    --navy: #1b2f5e;
    --band-light: #1c2a45;
    --band-plum: #211c35;
    --red: #d52b34;
    --white: #ffffff;
    --grey-text: #555658;
    --divider: #b9b9b9;
  }
  * { margin: 0; padding: 0; box-sizing: border-box; }
  html, body { width: 1200px; height: 1200px; overflow: hidden; }
  body {
    background: var(--backdrop);
    font-family: "Inter", sans-serif;
    position: relative;
  }
  .card {
    position: absolute;
    left: 179px;
    width: 861px;
    height: 496px;
    overflow: hidden;
  }
  .card-front { top: 84px; background: var(--navy-deep); }
  .card-back  { top: 621px; background: var(--white); }

  .front-bands { position: absolute; inset: 0; width: 100%; height: 100%; }

  .front-brand {
    position: absolute;
    left: 0; right: 0;
    top: 168px;
    text-align: center;
    color: var(--white);
    font-weight: 800;
    font-size: 42px;
    line-height: 1.15;
    letter-spacing: 0.5px;
  }
  .front-rule {
    position: absolute;
    top: 451px;
    height: 3px;
    width: 102px;
    background: var(--red);
  }
  .front-rule.left { left: 287px; }
  .front-rule.right { left: 472px; }
  .front-dot {
    position: absolute;
    left: 420px; top: 443px;
    width: 20px; height: 20px;
    border-radius: 50%;
    background: var(--white);
  }

  .back-brand {
    position: absolute;
    left: 60px; top: 190px;
    width: 240px;
    text-align: center;
    color: var(--navy);
    font-weight: 800;
    font-size: 30px;
    line-height: 1.15;
  }
  .back-divider {
    position: absolute;
    left: 329px; top: 132px;
    width: 2px; height: 236px;
    background: var(--divider);
  }
  .contact-block { position: absolute; left: 355px; top: 124px; }
  .person-name {
    color: var(--navy);
    font-weight: 700;
    font-size: 36px;
    line-height: 1.1;
    letter-spacing: 0.5px;
  }
  .person-title {
    color: var(--grey-text);
    font-weight: 500;
    font-size: 27px;
    letter-spacing: 3px;
    margin-top: 2px;
  }
  .contact-list { list-style: none; margin-top: 54px; }
  .contact-list li {
    display: flex;
    align-items: center;
    height: 42px;
    color: var(--grey-text);
    font-size: 23px;
    font-weight: 500;
    letter-spacing: 1.8px;
  }
  .contact-list svg { width: 30px; height: 30px; margin-right: 14px; flex: none; fill: none; stroke: var(--navy); stroke-width: 2.2; }
  .accent { color: var(--red); }
</style>
</head>
<body>

<section class="card card-front">
  <svg class="front-bands" viewBox="0 0 861 496" preserveAspectRatio="none" aria-hidden="true">
    <polygon points="92,0 272,0 861,330 861,445" fill="var(--band-light)"/>
    <polygon points="0,49 0,144 560,496 760,496" fill="var(--band-plum)"/>
    <polygon points="769,0 589,0 0,330 0,445" fill="var(--band-light)"/>
    <polygon points="861,49 861,144 301,496 101,496" fill="var(--band-plum)"/>
  </svg>
  <div class="front-brand">Larkspur Ridge<br>Management</div>
  <span class="front-rule left"></span>
  <span class="front-dot"></span>
  <span class="front-rule right"></span>
</section>

<section class="card card-back">
  <div class="back-brand">Larkspur Ridge<br>Management</div>
  <span class="back-divider"></span>
  <div class="contact-block">
    <h1 class="person-name">Name Surename</h1>
    <p class="person-title">Chief Financial Officer</p>
    <ul class="contact-list">
      <li>
        <svg viewBox="0 0 24 24"><path d="M5 3h4l2 5-2.5 1.5a11 11 0 0 0 6 6L16 13l5 2v4a2 2 0 0 1-2 2A17 17 0 0 1 3 5a2 2 0 0 1 2-2z"/></svg>
        (555) 817-3094
      </li>
      <li>
        <svg viewBox="0 0 24 24"><rect x="3" y="6" width="18" height="12"/><path d="M3 6l9 7 9-7"/></svg>
        info@larkridgemgmt.example
      </li>
      <li>
        <svg viewBox="0 0 24 24"><circle cx="12" cy="12" r="9"/><ellipse cx="12" cy="12" rx="4" ry="9"/><path d="M3 12h18M4.5 7.5h15M4.5 16.5h15"/></svg>
        www.<span class="accent">larkridgemgmt</span>.example
      </li>
    </ul>
  </div>
</section>

</body>
</html>
```